Business Cards Needed for Innovative Healthcare Marketing Company

We are a marketing company focused on healthcare. Our company is all about rebranding yourself renewing your image and generating results. The phoenix stands for "reborn" or "rising" which we provide new brands for our clients we take their old brands and renew it with creativity and innovation. I am looking for a business card with color dimension. I have attached an example of a card I think has the look and feel of what I am trying to accomplish. I like that the card example has black and grey font colors, I like the font placement and the small logo, I really like the use of the colors on the right those are the colors of my logo. My logo is phoenix so maybe incorporating flames similar to that design. I would like the back a solid color maybe red with an opaque version of the logo and website. As a marketing company I am always open to creative liberty!

Target Market(s)

Doctors and business professionals.

Industry/Entity Type

Marketing

Contact Information for Business Card

Vornaly Health Care Marketing
Marnie Okonski- CEO
#(502)638-2947
email-marnie@vornaly.com
website- vornaly.com

Font styles to use
Sans Serif

Colors
ec1f27
f37122
ffc214
fbed22
fbf289
f04a50

Requirements
Must have
• The logo and required information
Nice to have
• icons by the information
Should not have
• child like font

```html
<!DOCTYPE html>
<html lang="en">
<head>
<meta charset="utf-8">
<title>Vornaly Health Care Marketing – Business Card</title>
<link href="https://fonts.googleapis.com/css2?family=Montserrat:wght@300;400;600;700&display=swap" rel="stylesheet">
<style>
  :root {
    --red: #ec1f27;
    --red-deep: #c81a22;
    --coral: #f04a50;
    --orange: #f37122;
    --amber: #ffc214;
    --ink: #3a3a3a;
    --grey: #8a8a8a;
    --paper: #ffffff;
    --stage: #e9e7e4;
  }
  * { box-sizing: border-box; margin: 0; padding: 0; }
  html, body { width: 1200px; height: 1023px; overflow: hidden; }
  body {
    background: var(--stage);
    font-family: "Montserrat", sans-serif;
    display: flex;
    flex-direction: column;
    align-items: center;
    justify-content: center;
    gap: 36px;
  }
  .card {
    width: 820px;
    height: 468px;
    border-radius: 22px;
    position: relative;
    overflow: hidden;
    box-shadow: 0 10px 30px rgba(0,0,0,.18);
  }

  /* Front */
  .card--front { background: var(--paper); }
  .brand {
    position: absolute; left: 64px; top: 70px;
    display: flex; align-items: center; gap: 18px;
  }
  .brand__dot {
    width: 64px; height: 64px; border-radius: 50%;
    background: var(--red);
  }
  .brand__name {
    font-weight: 300; font-size: 44px; letter-spacing: 2px;
    color: var(--red); line-height: 1;
  }
  .brand__tagline {
    font-size: 11px; letter-spacing: 1.5px; color: var(--grey);
    margin-top: 6px; border-top: 1px solid #d8d8d8; padding-top: 4px;
  }
  .person { position: absolute; left: 64px; top: 218px; }
  .person__name { font-weight: 700; font-size: 34px; color: var(--red-deep); }
  .person__title { font-size: 16px; color: var(--orange); margin-top: 2px; }
  .contacts {
    position: absolute; left: 64px; top: 310px;
    list-style: none; display: flex; flex-direction: column; gap: 12px;
  }
  .contacts li {
    display: flex; align-items: center; gap: 14px;
    font-size: 17px; color: var(--ink);
  }
  .contacts svg { width: 26px; height: 26px; flex: none; }
  .mark-area {
    position: absolute; right: 70px; top: 40px;
    width: 330px; height: 330px; border-radius: 50%;
    background: radial-gradient(circle at 40% 40%, rgba(255,194,20,.35), rgba(243,113,34,.25) 55%, rgba(236,31,39,.12) 100%);
  }

  /* Back */
  .card--back {
    background: radial-gradient(ellipse at 40% 30%, #f0333a, var(--red) 45%, #d41a22 100%);
    color: #fff;
    display: flex; flex-direction: column; align-items: center; justify-content: center;
    text-align: center;
  }
  .back__dot {
    width: 110px; height: 110px; border-radius: 50%;
    background: rgba(255,255,255,.85); margin-bottom: 28px;
  }
  .back__name { font-weight: 300; font-size: 70px; letter-spacing: 4px; line-height: 1; }
  .back__tagline { font-weight: 600; font-size: 20px; letter-spacing: 1px; margin-top: 10px; }
  .back__url { font-size: 16px; letter-spacing: 4px; margin-top: 20px; }
</style>
</head>
<body>

  <section class="card card--front">
    <div class="brand">
      <span class="brand__dot"></span>
      <div>
        <div class="brand__name">VORNALY</div>
        <div class="brand__tagline">HEALTHCARE MARKETING</div>
      </div>
    </div>

    <div class="person">
      <div class="person__name">Marnie Okonski</div>
      <div class="person__title">Title</div>
    </div>

    <ul class="contacts">
      <li>
        <svg viewBox="0 0 26 26" aria-hidden="true"><rect width="26" height="26" rx="6" fill="#ec1f27"/><path d="M9 7c-1 1-2 2-1 4 1 3 4 6 7 7 2 1 3 0 4-1l-2-2-2 1c-2-1-3-2-4-4l1-2z" fill="#fff"/></svg>
        <span>(502)638-2947</span>
      </li>
      <li>
        <svg viewBox="0 0 26 26" aria-hidden="true"><rect width="26" height="26" rx="6" fill="#ec1f27"/><rect x="6" y="8" width="14" height="10" rx="1" fill="none" stroke="#fff" stroke-width="1.8"/><path d="M6 9l7 5 7-5" fill="none" stroke="#fff" stroke-width="1.8"/></svg>
        <span>marnie@vornaly.com</span>
      </li>
      <li>
        <svg viewBox="0 0 26 26" aria-hidden="true"><g fill="none" stroke="#ec1f27" stroke-width="1.6"><circle cx="13" cy="13" r="11"/><ellipse cx="13" cy="13" rx="5" ry="11"/><path d="M2 13h22M4 7h18M4 19h18"/></g></svg>
        <span>www.vornaly.com</span>
      </li>
    </ul>

    <div class="mark-area" role="img" aria-label="Brand mark decoration in red, orange and amber tones"></div>
  </section>

  <section class="card card--back">
    <span class="back__dot"></span>
    <div class="back__name">VORNALY</div>
    <div class="back__tagline">HEALTHCARE MARKETING</div>
    <div class="back__url">www.vornaly.com</div>
  </section>

</body>
</html>
```